Real Estate Company Needs Business Card Designed

We need a business card design for a new real estate company based in Campbell, CA (Silicon Valley). We plan to improve the residential real estate industry by using technology to improve customer experience. We would like to see designs that use a black background. The final design should communicate sophistication and customer service, as well as stability and technology.

Industry/Entity Type

Real Estate

Requirements
Must have
• Black background

```html
<!DOCTYPE html>
<html lang="en">
<head>
<meta charset="utf-8">
<title>Business Card</title>
<link href="https://fonts.googleapis.com/css2?family=Arimo:wght@400;700&display=swap" rel="stylesheet">
<style>
  :root {
    --page: #dcdcdc;
    --card-dark: #1e1e1f;
    --card-mid: #303031;
    --brand-white: #e9eaec;
    --info-blue: #1d6fb8;
    --rule-blue: #1b5f9c;
    --web-red: #d0124a;
  }
  * { margin: 0; padding: 0; box-sizing: border-box; }
  html, body {
    width: 1200px;
    height: 750px;
    overflow: hidden;
    background: var(--page);
    font-family: "Arimo", Arial, sans-serif;
  }
  .card {
    position: absolute;
    left: 100px;
    top: 89px;
    width: 1000px;
    height: 572px;
    border-radius: 40px;
    background: linear-gradient(160deg, var(--card-mid) 0%, var(--card-dark) 55%, #161617 100%);
    overflow: hidden;
  }
  .identity {
    position: absolute;
    left: 60px;
    top: 205px;
    width: 360px;
    text-align: center;
  }
  .brand-name {
    color: var(--brand-white);
    font-weight: 400;
    font-size: 36px;
    letter-spacing: 2px;
    margin-bottom: 48px;
  }
  .person-name {
    color: var(--info-blue);
    font-weight: 700;
    font-size: 44px;
    line-height: 1;
  }
  .person-role {
    color: var(--info-blue);
    font-weight: 700;
    font-size: 30px;
    margin-top: 4px;
  }
  .divider {
    position: absolute;
    left: 470px;
    top: 80px;
    width: 2px;
    height: 340px;
    background: var(--rule-blue);
  }
  .contact {
    position: absolute;
    left: 520px;
    top: 90px;
    color: var(--info-blue);
    font-weight: 700;
    font-size: 29px;
    line-height: 40px;
  }
  .contact .address { margin-bottom: 34px; }
  .website {
    position: absolute;
    left: 430px;
    top: 452px;
    color: var(--web-red);
    font-weight: 700;
    font-size: 58px;
    letter-spacing: 1px;
    white-space: nowrap;
  }
</style>
</head>
<body>
  <div class="card">
    <div class="identity">
      <div class="brand-name">CORVENNA</div>
      <div class="person-name">your name</div>
      <div class="person-role">posting</div>
    </div>
    <div class="divider"></div>
    <div class="contact">
      <div class="address">
        <div>xxxxxx xxxxxxxx</div>
        <div>xxxxx xxxxx xxxxx</div>
        <div>xxxxxxxxxx</div>
      </div>
      <div class="phone">ph : xxxxxxxxxx</div>
      <div class="email">email : xxxxxxxxxxxx</div>
    </div>
    <div class="website">www.yoursite.com</div>
  </div>
</body>
</html>
```